Pine Ridge Traders, LLC- Global Beverage Company with 100% Cold Chain Logistics

Hey All, My Name is Tom, I am a young business owner in a competitive export space, but my niche is that I am shipping all of my beer around the world, "100% Cold Chain". This model is more costly, but it protects the integrity of the beer itself and will give folks in foreign countries the best representation of what US Craft Beer has to offer.

I am not a branding guy and don't claim to be one, I am a salesperson first, and will be referring to all of you to create something great that will be memorable.

I am looking for a basic Business Card Design for my Craft Beer Export company. I sell US Craft Beer in several countries around the globe. Austrailia, China, Taiwan, Chile, France, New Zealand... to name a few.

I am looking for a sleek, modern, and fresh design. Quickly!

Thanks for your consideration!

Cheers,

Tom

Target Market(s)

International

Contact Information for Business Card

Tom Reilly
Founder- World Brew Guy
Tom@PineRidgeTraders.example
@WorldBrewGuy- Instagram only
www.Pineridgetraders.example
@PineRidgeTradersAU- Instagram Only

Font styles to use
Serif

Colors
0592cd
ffffff

Requirements
Must have
• Name-
• Title-
• Email-
• Social Media Handle-
• Company Website-
Nice to have
• Nice Logo/ Images on Card
Should not have
• Tacky Beer Images

```html
<!DOCTYPE html>
<html lang="en">
<head>
<meta charset="utf-8">
<title>Pine Ridge Traders — Business Card</title>
<link href="https://fonts.googleapis.com/css2?family=Roboto+Slab:wght@400;700&display=swap" rel="stylesheet">
<style>
  :root {
    --stage: #1d1d1f;
    --brand-blue: #0592cd;
    --deep-blue: #04648c;
    --map-blue: #2aa6da;
    --paper: #ffffff;
    --title-blue: #04648c;
    --icon-ring: #0592cd;
  }
  html, body {
    margin: 0;
    width: 1200px;
    height: 1200px;
    overflow: hidden;
    background: var(--stage);
    font-family: "Roboto Slab", Georgia, serif;
  }
  .stage {
    position: relative;
    width: 1200px;
    height: 1200px;
  }
  .card {
    position: absolute;
    left: 170px;
    width: 860px;
    height: 490px;
    overflow: hidden;
  }
  .card--front { top: 90px; background: var(--brand-blue); }
  .card--back { top: 620px; background: var(--paper); }

  .world-map {
    position: absolute;
    left: 150px; top: 30px;
    width: 690px; height: 430px;
    border-radius: 40px;
    background: radial-gradient(ellipse at center, var(--map-blue) 0%, rgba(42,166,218,0.35) 60%, rgba(42,166,218,0) 100%);
  }
  .brand-lockup {
    position: absolute;
    display: flex;
    align-items: center;
    gap: 14px;
    font-weight: 700;
    letter-spacing: 2px;
    text-transform: uppercase;
    line-height: 1.15;
    font-size: 30px;
  }
  .brand-lockup__mark {
    width: 46px; height: 46px;
    border-radius: 50%;
    flex: none;
    box-sizing: border-box;
  }
  .card--front .brand-lockup {
    left: 50%; top: 50%;
    transform: translate(-50%, -50%);
    color: var(--paper);
  }
  .card--front .brand-lockup__mark { border: 3px solid var(--paper); }
  .card--back .brand-lockup {
    left: 48px; top: 96px;
    color: var(--brand-blue);
  }
  .card--back .brand-lockup__mark { background: var(--brand-blue); width: 56px; height: 56px; }

  .wave-art { position: absolute; left: 0; top: 0; }

  .identity {
    position: absolute;
    right: 70px; top: 76px;
    text-align: right;
  }
  .identity__name {
    margin: 0;
    color: var(--brand-blue);
    font-size: 36px;
    font-weight: 700;
    letter-spacing: 1px;
  }
  .identity__title {
    margin: 6px 0 0;
    color: var(--title-blue);
    font-size: 20px;
    font-weight: 400;
    letter-spacing: 0.5px;
  }

  .contact-list {
    position: absolute;
    right: 40px; top: 324px;
    margin: 0; padding: 0;
    list-style: none;
  }
  .contact-list__item {
    display: flex;
    justify-content: flex-end;
    align-items: center;
    gap: 12px;
    height: 31px;
    color: var(--paper);
    font-size: 16px;
    letter-spacing: 0.3px;
  }
  .contact-icon {
    width: 26px; height: 26px;
    border-radius: 50%;
    background: var(--paper);
    border: 3px solid var(--deep-blue);
    box-sizing: border-box;
    display: flex; align-items: center; justify-content: center;
    flex: none;
  }
</style>
</head>
<body>
<main class="stage">

  <section class="card card--front" aria-label="Card front">
    <div class="world-map" role="img" aria-label="Faint world map across the card"></div>
    <div class="brand-lockup">
      <span class="brand-lockup__mark"></span>
      <span>Pine Ridge<br>Traders, LLC</span>
    </div>
  </section>

  <section class="card card--back" aria-label="Card back">
    <svg class="wave-art" width="860" height="490" viewBox="0 0 860 490" aria-hidden="true">
      <path d="M0,300 C200,360 360,390 520,330 C640,285 760,290 860,320 L860,490 L0,490 Z" fill="var(--brand-blue)"/>
      <path d="M0,235 C120,300 260,350 440,345 C330,360 160,330 0,290 Z" fill="var(--deep-blue)"/>
      <path d="M0,290 C160,330 330,360 440,345 C300,378 140,355 0,318 Z" fill="var(--paper)"/>
      <path d="M60,372 C200,410 330,405 430,368 C330,398 200,398 60,372 Z" fill="var(--paper)"/>
    </svg>

    <div class="brand-lockup">
      <span class="brand-lockup__mark"></span>
      <span>Pine Ridge<br>Traders, LLC</span>
    </div>

    <div class="identity">
      <h1 class="identity__name">Tom Reilly</h1>
      <p class="identity__title">Founder- World Brew Guy</p>
    </div>

    <ul class="contact-list">
      <li class="contact-list__item">+61 3 9000 4127
        <span class="contact-icon"><svg width="12" height="12" viewBox="0 0 24 24"><path d="M6.6 10.8a15 15 0 0 0 6.6 6.6l2.2-2.2a1 1 0 0 1 1-.25 11.4 11.4 0 0 0 3.6.6 1 1 0 0 1 1 1V20a1 1 0 0 1-1 1A17 17 0 0 1 3 4a1 1 0 0 1 1-1h3.5a1 1 0 0 1 1 1c0 1.25.2 2.45.6 3.6a1 1 0 0 1-.25 1z" fill="var(--deep-blue)"/></svg></span>
      </li>
      <li class="contact-list__item">Tom@PineRidgeTraders.example
        <span class="contact-icon"><svg width="12" height="12" viewBox="0 0 24 24"><rect x="2" y="5" width="20" height="14" fill="none" stroke="var(--deep-blue)" stroke-width="2"/><path d="M2 5l10 8 10-8" fill="none" stroke="var(--deep-blue)" stroke-width="2"/></svg></span>
      </li>
      <li class="contact-list__item">www.Pineridgetraders.example
        <span class="contact-icon"><svg width="12" height="12" viewBox="0 0 24 24" fill="none" stroke="var(--deep-blue)" stroke-width="2"><circle cx="12" cy="12" r="10"/><ellipse cx="12" cy="12" rx="4" ry="10"/><path d="M2 12h20M4 7h16M4 17h16"/></svg></span>
      </li>
      <li class="contact-list__item">@WorldBrewGuy
        <span class="contact-icon"></span>
      </li>
      <li class="contact-list__item">@PineRidgeTradersAU
        <span class="contact-icon"></span>
      </li>
    </ul>
  </section>

</main>
</body>
</html>
```